A fantastic website for a physio

We are looking for an eye catching website which can attract as many customer as possible.
We have logo designed and ready to be used in the website.
Please use the green and blue which is used in our logo for the preferred colors.
The following are the designs that I Iike:
http://www.bendwellclinic.com.au/
http://www.tullowayrehab.com.au/
We will be having other services including massage therapy, Psychology and podiatrist. You can find information about podiatry in our condition sheet.
for the address you can put Shop 7/482 Castellan Road, Dunmore Vale. It might change but for now you can leave it until I confirm that in the next couple of days.

Logo file can be downloaded here:
https://www.filecrate.example/s/qz4mpl82kvhrtx/Logo1511.jpg?dl=0

Target Market(s)

Infant to old people.
We speak Farsi.

Industry/Entity Type

Physical Therapy

Number of Pages Required

5+ page

Font styles to use
Serif

Colors
33a6d7
abd037
e667a6

Requirements
Must have
• Home, About , our services, Conditions we treat and contact
• For home page and contacts we would like a tab that can connect to another website(bookvora) for online booking. We would like the patient's to be able to leave us massage or leave their email for monthly news letter. For the condition we treat you can use the condition sheets I have attached. For about us and home page you can use brochure I have attached.
• The other things should have include: in-line contact form, Clinic Map, clinic hours, newsletter sign-up etc, schema rich contact information
• Social media connection to our Facebook, Instagram and linked in
Nice to have
• Search engine optimization for Merrylands and Parramatta physiotherapy.
• We can speak English and Farsi. So is nice to have an information tab for Farsi speaking people. I can provide you with the texts.

```html
<!DOCTYPE html>
<html lang="en">
<head>
<meta charset="utf-8">
<title>Linkwell Physiotherapy</title>
<link href="https://fonts.googleapis.com/css2?family=Raleway:wght@400;600;700&family=Open+Sans:wght@400;600;700&display=swap" rel="stylesheet">
<style>
:root{
  --blue:#2ea3da;
  --blue-light:#4cc0ee;
  --blue-dark:#1b6f9b;
  --green:#8cc63f;
  --ink:#333;
  --muted:#777;
  --grey-bg:#f1f1f1;
  --footer:#232323;
  --footer-deep:#1a1a1a;
}
*{box-sizing:border-box;margin:0;padding:0}
html,body{width:746px;height:1200px;overflow:hidden}
body{position:relative;background:#fff;font-family:"Open Sans",sans-serif;color:var(--ink)}
.abs{position:absolute}
svg{display:block}

/* top bar */
.topbar{left:0;top:0;width:746px;height:20px;background:#f5f5f5;border-top:2px solid var(--blue);font-size:5px;color:#999}
.topbar .item{position:absolute;top:6px;display:flex;align-items:center;gap:3px}
.topbar .social{position:absolute;top:5px;right:146px;display:flex;gap:5px}
.topbar .social span{width:6px;height:6px;background:#ccc}
.topbar .social span.on{background:var(--blue)}

/* header */
.header{left:0;top:20px;width:746px;height:44px;background:#fff}
.brand{position:absolute;left:144px;top:8px;display:flex;align-items:center;gap:5px}
.brand .dot{width:26px;height:26px;border-radius:50%;background:var(--blue)}
.brand .name{font-family:"Raleway",sans-serif;font-weight:600;font-size:12px;color:var(--green);line-height:1.1}
.nav{position:absolute;right:146px;top:18px;display:flex;gap:16px;font-size:5.6px;color:#888;align-items:center}
.nav .active{color:var(--green)}

/* hero */
.hero{left:0;top:64px;width:746px;height:274px;background:linear-gradient(120deg,#8d8d8d 0%,#d9d9d9 40%,#b5b5b5 70%,#e8e8e8 100%)}
.hero .accent{position:absolute;left:120px;top:40px;width:200px;height:200px;background:radial-gradient(circle,rgba(40,110,200,.55),rgba(40,110,200,0) 70%)}
.hero h1{position:absolute;right:148px;top:124px;text-align:right;font-family:"Raleway",sans-serif;font-weight:400;font-size:19px;line-height:23px;color:#222}
.btn-green{background:var(--green);color:#fff;font-size:5px;font-weight:700;text-transform:uppercase;display:flex;align-items:center;justify-content:center;border-bottom:2px solid #6ea12c}
.hero .btn-green{position:absolute;left:534px;top:253px;width:66px;height:20px}
.hero .arrow{position:absolute;top:129px;width:18px;height:18px;border-radius:50%;border:1px solid rgba(255,255,255,.8)}
.dots{position:absolute;left:378px;top:328px;display:flex;gap:2px}
.dots span{width:5px;height:5px;background:#fff}
.dots span:first-child{background:none;border:1px solid #fff}

/* booking */
.booking{left:0;top:338px;width:746px;height:74px;background:var(--blue)}
.booking .label{position:absolute;left:0;top:0;width:251px;height:74px;background:#2a95c8;color:#fff;text-align:center;font-family:"Raleway",sans-serif;font-size:9.5px;line-height:9px;padding-left:100px;padding-top:24px}
.booking .label svg{margin:0 auto 4px}
.field{position:absolute;height:15px;background:var(--blue-light);color:#e6f6fd;font-size:4.8px;padding-left:8px;display:flex;align-items:center}
.field.outline{background:none;border:1px solid #9ddcf5}

/* services */
.services{left:0;top:412px;width:746px;height:200px;background:var(--grey-bg)}
.section-title{position:absolute;font-family:"Raleway",sans-serif;font-weight:400;font-size:14px;color:#222}
.section-title::after{content:"";position:absolute;left:50%;bottom:-9px;width:24px;margin-left:-12px;height:1px;background:#bbb}
.service{position:absolute;top:64px;width:150px;text-align:center}
.service .icon{width:50px;height:50px;border-radius:50%;margin:0 auto;display:flex;align-items:center;justify-content:center;border:2px solid #fff;box-shadow:0 0 0 1px #ddd}
.service h3{font-family:"Raleway",sans-serif;font-weight:400;font-size:10px;color:#444;margin-top:10px}
.service p{font-size:5.2px;line-height:8px;color:#666;margin-top:5px}

/* articles */
.articles-title{left:145px;top:632px;font-family:"Raleway",sans-serif;font-size:14px;color:#222}
.articles-title::after{content:"";position:absolute;left:0;bottom:-9px;width:16px;height:1px;background:#bbb}
.pager{position:absolute;top:636px;display:flex;gap:1px;left:580px}
.pager span{width:10px;height:10px;border:1px solid var(--blue)}
.pager span:first-child{background:var(--blue)}
.article{position:absolute;top:665px;width:138px}
.article .photo{height:78px}
.article h4{font-size:5.4px;font-weight:700;margin-top:7px;color:#222}
.article .meta{font-size:4.8px;color:#888;margin-top:3px;display:flex;gap:3px;align-items:center}
.article p{font-size:4.8px;line-height:9.5px;color:#888;margin-top:5px}
.article .date{position:absolute;left:8px;top:63px;color:#fff;font-size:4.4px;font-weight:700}

/* info boxes */
.info{left:146px;top:823px;width:454px;height:99px;display:flex}
.info .box{height:99px;color:#fff;padding:22px 0 0 12px;font-family:"Raleway",sans-serif;font-size:8px;line-height:8px}
.info .box .open{font-family:"Open Sans",sans-serif;font-size:4.6px;opacity:.7;margin-top:14px}
.hours{width:144px;background:var(--blue-dark);padding:22px 12px 0 12px!important}
.hours h3{font-size:8px;font-weight:700;display:flex;gap:5px;align-items:center;margin-bottom:9px}
.hours .row{display:flex;justify-content:space-between;font-family:"Open Sans",sans-serif;font-size:4.8px;padding:3px 0 4px;border-bottom:1px solid rgba(255,255,255,.08)}
.hours .row b{font-weight:700}

/* footer */
.footer{left:0;top:948px;width:746px;height:217px;background:var(--footer)}
.footer .title{position:absolute;left:0;width:746px;top:19px;text-align:center;font-family:"Raleway",sans-serif;font-size:14px;color:#fff;letter-spacing:.5px}
.footer .title::after{content:"";position:absolute;left:361px;top:27px;width:24px;height:1px;background:#777}
.contact-strip{position:absolute;left:144px;top:75px;width:24px;height:105px;background:#191919}
.contact-strip svg{position:absolute;left:7px}
.contact-info{position:absolute;left:178px;top:78px;color:#ccc;font-size:4.6px;line-height:10px}
.contact-info h5{color:#fff;font-size:5px;font-weight:700;margin-top:8px}
.contact-info h5:first-child{margin-top:0}
.form{position:absolute;left:299px;top:75px;width:276px;height:105px;border:1px solid #3a3a3a;background:#262626}
.form .row{display:flex;height:18px;border-bottom:1px solid #3a3a3a;font-size:4.6px;color:#888}
.form .row div{flex:1;padding:6px 4px}
.form .row div+div{border-left:1px solid #3a3a3a}
.form .msg{padding:6px 4px;font-size:4.6px;color:#888}
.send{position:absolute;left:575px;top:75px;width:24px;height:105px;background:var(--green);display:flex;align-items:center;justify-content:center}
.bottombar{left:0;top:1165px;width:746px;height:35px;background:var(--footer-deep)}
.bottombar .social{position:absolute;left:144px;top:10px;display:flex;gap:3px}
.bottombar .social span{width:15px;height:14px;border:1px solid #888}
.bottombar .copy{position:absolute;right:146px;top:14px;font-size:5px;color:#bbb}
</style>
</head>
<body>

<div class="abs topbar">
  <div class="item" style="left:146px">
    <svg width="6" height="5" viewBox="0 0 6 5"><rect x="0.3" y="0.3" width="5.4" height="4.4" fill="none" stroke="#aaa" stroke-width=".6"/><path d="M.3 .3L3 2.6 5.7.3" fill="none" stroke="#aaa" stroke-width=".6"/></svg>
    support@yoursite.com
  </div>
  <div class="item" style="left:250px">
    <svg width="5" height="5" viewBox="0 0 5 5"><path d="M1 .3l1 1.2-.6.7c.4.8.9 1.3 1.5 1.6l.7-.6 1.1 1-.7.8C2.4 4.8.2 2.6.3 1z" fill="#aaa"/></svg>
    +440 812 004 517
  </div>
  <div class="item" style="left:479px">Language: English &nbsp;⌄</div>
  <div class="social"><span></span><span class="on"></span><span></span><span></span><span></span></div>
</div>

<header class="abs header">
  <div class="brand"><span class="dot"></span><span class="name">Linkwell<br>Physiotherapy</span></div>
  <nav class="nav">
    <span class="active">Home</span><span>About us</span><span>Services</span><span>Conditions we treat</span><span>Contact</span>
    <svg width="9" height="9" viewBox="0 0 9 9"><circle cx="3.8" cy="3.8" r="3" fill="none" stroke="#ccc"/><path d="M6 6l2.5 2.5" stroke="#ccc"/></svg>
  </nav>
</header>

<section class="abs hero" role="img" aria-label="Photo of a therapist applying a handheld shockwave device to a patient's shoulder">
  <div class="accent"></div>
  <span class="arrow" style="left:88px"></span>
  <span class="arrow" style="left:638px"></span>
  <h1>Learn about our Pain<br>Management Program</h1>
  <div class="btn-green">Read more</div>
  <div class="dots"><span></span><span></span><span></span><span></span></div>
</section>

<section class="abs booking">
  <div class="label">
    <svg width="12" height="12" viewBox="0 0 12 12"><rect x="1" y="2" width="10" height="9" fill="none" stroke="#fff"/><path d="M1 4.5h10M3.5 1v2M8.5 1v2M3 6.5h1M5.5 6.5h1M8 6.5h1M3 8.5h1M5.5 8.5h1M8 8.5h1" stroke="#fff"/></svg>
    Book An<br>Appointment
  </div>
  <div class="field outline" style="left:262px;top:14px;width:105px">Full Name</div>
  <div class="field" style="left:379px;top:14px;width:105px">Email Address</div>
  <div class="field" style="left:495px;top:14px;width:105px">Phone Number</div>
  <div class="field" style="left:262px;top:39px;width:105px">Appointment Date</div>
  <div class="field" style="left:379px;top:39px;width:105px">Doctor</div>
  <div class="abs" style="left:469px;top:39px;width:15px;height:15px;background:#2a8fc0"></div>
  <div class="abs btn-green" style="left:495px;top:38px;width:105px;height:15px">Make an appointment</div>
</section>

<section class="abs services">
  <h2 class="section-title" style="left:0;width:746px;text-align:center;top:26px">Our Services</h2>
  <div class="service" style="left:139px">
    <div class="icon" style="background:var(--blue)"><svg width="24" height="20" viewBox="0 0 24 20"><circle cx="13" cy="5" r="3" fill="#fff"/><rect x="2" y="13" width="20" height="3" rx="1" fill="#fff"/><path d="M6 12c2-4 6-5 10-3l-2 3z" fill="#fff"/></svg></div>
    <h3>Massage Therapy</h3>
    <p>Lorem ipsum dolor sit amet, consectetur adipiscing elit. Etiam ut tincidunt arcu. Suspendisse in justo eu mi bibendum varius.</p>
  </div>
  <div class="service" style="left:298px">
    <div class="icon" style="background:var(--green)"><svg width="22" height="22" viewBox="0 0 22 22"><circle cx="11" cy="10" r="7" fill="#fff"/><rect x="8" y="14" width="6" height="6" fill="#fff"/></svg></div>
    <h3>Psychology</h3>
    <p>Lorem ipsum dolor sit amet, consectetur adipiscing elit. Etiam ut tincidunt arcu. Suspendisse in justo eu mi bibendum varius.</p>
  </div>
  <div class="service" style="left:457px">
    <div class="icon" style="background:var(--blue)"><svg width="20" height="24" viewBox="0 0 20 24"><ellipse cx="10" cy="15" rx="5" ry="8" fill="#fff"/><circle cx="5" cy="4" r="2" fill="#fff"/><circle cx="9" cy="3" r="1.6" fill="#fff"/><circle cx="12.5" cy="3.6" r="1.4" fill="#fff"/><circle cx="15" cy="5.5" r="1.2" fill="#fff"/></svg></div>
    <h3>Podiatrist</h3>
    <p>Lorem ipsum dolor sit amet, consectetur adipiscing elit. Etiam ut tincidunt arcu. Suspendisse in justo eu mi bibendum varius.</p>
  </div>
</section>

<h2 class="abs articles-title">Latest Articles</h2>
<div class="pager"><span></span><span></span></div>

<article class="article" style="left:145px">
  <div class="photo" role="img" aria-label="Photo of a therapist's hands treating a patient's leg" style="background:linear-gradient(135deg,#5d544f,#9c8d84 50%,#2f3a3c)"></div>
  <span class="date">September,29 2016</span>
  <h4>voluptate velit esse cillum</h4>
  <div class="meta">● 0 Comments</div>
  <p>Mrs. Darling first heard of Peter when she was tidying up her children's minds. Lorem ipsum dolor sit</p>
</article>
<article class="article" style="left:303px">
  <div class="photo" role="img" aria-label="Photo of gloved hands examining a patient's foot" style="background:linear-gradient(135deg,#6f8ba6,#d8d4cc 55%,#9aa9b5)"></div>
  <h4>voluptate velit esse cillum</h4>
  <div class="meta">● 0 Comments</div>
  <p>Mrs. Darling first heard of Peter when she was tidying up her children's minds. Lorem ipsum dolor sit</p>
</article>
<article class="article" style="left:461px">
  <div class="photo" role="img" aria-label="Photo of a physiotherapist stretching a patient's leg on a treatment table" style="background:linear-gradient(135deg,#e8e2dc,#c9a994 45%,#8fc9bd 75%,#2d3a44)"></div>
  <h4>voluptate velit esse cillum</h4>
  <div class="meta">● 0 Comments</div>
  <p>Mrs. Darling first heard of Peter when she was tidying up her children's minds. Lorem ipsum dolor sit</p>
</article>

<section class="abs info">
  <div class="box hours">
    <h3><svg width="9" height="9" viewBox="0 0 9 9"><circle cx="4.5" cy="4.5" r="3.8" fill="none" stroke="#fff"/><path d="M4.5 2v2.5h2" fill="none" stroke="#fff"/></svg>Clinic hours</h3>
    <div class="row"><span>Monday - Friday</span><b>8.00 - 17.00</b></div>
    <div class="row"><span>Saturday</span><b>9.30 - 17.30</b></div>
    <div class="row"><span>Sunday</span><b>9.30 - 15.00</b></div>
  </div>
  <div class="box" style="width:78px;background:#1c7aa8">
    <svg width="9" height="9" viewBox="0 0 9 9"><rect x=".5" y="1.5" width="8" height="7" fill="none" stroke="#fff"/><path d="M.5 3.5h8M2.5 0v2M6.5 0v2" stroke="#fff"/></svg>
    <div style="margin-top:6px">Doctors<br>Timetable</div><div class="open">Open ›</div>
  </div>
  <div class="box" style="width:77px;background:#1e83b3">
    <svg width="10" height="8" viewBox="0 0 10 8"><rect x="0" y="0" width="10" height="8" fill="#fff"/><path d="M0 0l5 4 5-4" fill="none" stroke="#1e83b3"/></svg>
    <div style="margin-top:7px">Newsletter<br>Signup</div><div class="open">Open ›</div>
  </div>
  <div class="box" style="width:78px;background:#208dbf">
    <svg width="8" height="10" viewBox="0 0 8 10"><path d="M4 10C1 6 0 4.5 0 3.5a4 4 0 018 0C8 4.5 7 6 4 10z" fill="#fff"/><circle cx="4" cy="3.6" r="1.4" fill="#208dbf"/></svg>
    <div style="margin-top:6px">Find us on<br>Clinic Map</div><div class="open">Open ›</div>
  </div>
  <div class="box" style="width:77px;background:#2597cb">
    <svg width="10" height="9" viewBox="0 0 10 9"><rect x="2" y="0" width="8" height="6" rx="1" fill="none" stroke="#fff"/><rect x="0" y="2" width="7" height="5" rx="1" fill="#fff"/><path d="M1.5 7v2l2-2" fill="#fff"/></svg>
    <div style="margin-top:6px">Online<br>Consultation</div><div class="open">Open ›</div>
  </div>
</section>

<footer class="abs footer">
  <h2 class="title">QUICK CONTACT</h2>
  <div class="contact-strip">
    <svg style="top:16px" width="10" height="10" viewBox="0 0 10 10"><path d="M3 0h4v1l-1 1v3l2 2H5.5v3h-1V7H2l2-2V2L3 1z" fill="#fff"/></svg>
    <svg style="top:52px" width="10" height="10" viewBox="0 0 10 10"><rect width="10" height="10" rx="2" fill="#fff"/><path d="M3 2l1.3 1.5-.7.8c.5 1 1.1 1.6 1.9 2l.8-.7L7.8 7l-.8 1C4.5 8 2 5.5 2 3z" fill="#191919"/></svg>
    <svg style="top:87px" width="10" height="8" viewBox="0 0 10 8"><rect width="10" height="8" fill="#fff"/><path d="M0 0l5 4 5-4" fill="none" stroke="#191919"/></svg>
  </div>
  <div class="contact-info">
    <h5>ADDRESS</h5>
    <div>14 Varrin Street, Elmbrook Hill,<br>New South Wales, Australia</div>
    <h5>PHONE</h5>
    <div>+61.400 218 559</div>
    <h5 style="margin-top:14px">MAIL</h5>
    <div>hello@linkwellphysio.example</div>
  </div>
  <form class="form">
    <div class="row"><div>Name*</div><div>Mail*</div></div>
    <div class="msg">Type your message here ...</div>
  </form>
  <div class="send"><svg width="10" height="10" viewBox="0 0 10 10"><path d="M10 0L0 4l3 1.5L8 2 4 6v4l2-3 2 2z" fill="#fff"/></svg></div>
</footer>

<div class="abs bottombar">
  <div class="social"><span></span><span></span><span></span><span></span><span></span></div>
  <div class="copy">Copyrights 2016 © Yoursite, All rights reserved</div>
</div>

</body>
</html>
```